Kestrova Physical Therapy Website

I would need a clean modern website built to showcase my Physical therapy brand and services. I would need a simple but descriptive website that can ultimately connect my patients to my electronic medical portal so they may book an appointment..

```html
<!DOCTYPE html>
<html lang="en">
<head>
<meta charset="utf-8">
<title>Kestrova Physical Therapy &amp; Wellness</title>
<link href="https://fonts.googleapis.com/css2?family=Montserrat:wght@400;500;600;700&family=Lato:ital,wght@0,400;0,700;1,400&display=swap" rel="stylesheet">
<style>
:root{
  --teal:#1f8b8a;
  --teal-dark:#137c79;
  --teal-deep:#0f6b68;
  --green:#7cc142;
  --green-dark:#6aae33;
  --indigo:#4b5fb3;
  --ink:#2b2f36;
  --text:#555a62;
  --muted:#8a9098;
  --pale:#eef2f5;
  --white:#ffffff;
}
*{box-sizing:border-box;margin:0;padding:0}
html,body{width:1200px;height:4367px;overflow:hidden}
body{font-family:'Montserrat',sans-serif;color:var(--ink);background:var(--white);position:relative}
.abs{position:absolute}
section,header,footer{position:absolute;left:0;width:1200px;overflow:hidden}

/* header */
.site-header{top:0;height:114px;background:var(--white);overflow:visible;z-index:5}
.logo-badge{position:absolute;left:96px;top:0;width:196px;height:172px;border-radius:0 0 98px 98px;background:var(--white);display:flex;flex-direction:column;align-items:center;justify-content:center;gap:6px}
.logo-badge .dot{width:34px;height:34px;border-radius:50%;background:var(--teal)}
.logo-badge .name{font-weight:700;font-size:27px;color:var(--teal);letter-spacing:.5px}
.main-nav{position:absolute;top:70px;left:0;font-size:12px;font-weight:600;color:var(--ink)}
.main-nav a{position:absolute;white-space:nowrap;text-decoration:none;color:inherit}
.main-nav a.active{color:var(--teal)}
.main-nav a.active::after{content:"";position:absolute;left:-4px;right:-4px;top:38px;height:3px;background:var(--green)}
.call-btn{position:absolute;left:788px;top:0;width:266px;height:38px;background:var(--green-dark);color:var(--white);font-size:12px;font-weight:700;display:flex;align-items:center;justify-content:center;gap:6px;letter-spacing:.5px}

/* hero */
.hero{top:114px;height:616px}
.hero-photo{position:absolute;inset:0;background:linear-gradient(100deg,#f3f4f6 0%,#e6e8ea 35%,#c9cfd3 55%,#b7bcbf 75%,#d6d9dc 100%)}
.hero-title{position:absolute;left:105px;top:196px;font-weight:700;font-size:43px;color:var(--teal);letter-spacing:2px;line-height:1}
.hero-sub{position:absolute;left:105px;top:250px;font-weight:700;font-size:29px;color:var(--green);letter-spacing:2px}
.hero-text{position:absolute;left:110px;top:294px;font-size:14px;line-height:27px;color:var(--text)}
.btn{display:flex;align-items:center;justify-content:center;border-radius:30px;font-weight:700;font-size:13px;letter-spacing:1px;color:var(--white);background:var(--green-dark)}
.hero .btn{position:absolute;left:110px;top:367px;width:231px;height:48px}
.slider-arrow{position:absolute;top:256px;width:22px;height:36px}
.booking{position:absolute;left:741px;top:77px;width:340px;height:414px;background:var(--teal);padding:34px 35px 0}
.booking h2{font-size:19px;font-weight:700;color:var(--white);text-align:center;letter-spacing:1.5px;margin-bottom:18px}
.booking .field{height:36px;background:var(--white);margin-bottom:10px;font-size:11px;color:var(--text);padding:11px 20px}
.booking .field.tall{height:71px}
.booking .submit{height:36px;background:var(--green);color:var(--white);font-family:'Lato',sans-serif;font-weight:700;font-size:15px;display:flex;align-items:center;justify-content:center;margin-top:16px}

/* why choose */
.why{top:730px;height:592px;background:#f4f6f8}
.why-photo{position:absolute;left:0;top:0;width:630px;height:592px;background:linear-gradient(135deg,#dfe3e6,#b9c4cb 50%,#8fb7c9);clip-path:polygon(0 0,630px 0,415px 592px,0 592px)}
.section-heading{font-size:27px;font-weight:500;letter-spacing:1px;color:var(--ink)}
.section-heading strong{font-weight:700;color:var(--teal)}
.why .section-heading{position:absolute;left:617px;top:134px}
.rule{position:absolute;height:3px;background:var(--green)}
.why .lead{position:absolute;left:620px;top:193px;width:460px;font-size:13px;line-height:24px;color:var(--text)}
.feature{position:absolute;width:250px;display:flex;gap:12px}
.feature .icon{flex:none;width:74px;height:74px;border-radius:50%;background:linear-gradient(135deg,var(--green),var(--teal));display:flex;align-items:center;justify-content:center}
.feature h3{font-family:'Lato',sans-serif;font-size:16px;font-weight:700;color:var(--ink);margin:10px 0 6px}
.feature p{font-family:'Lato',sans-serif;font-size:11px;line-height:17px;color:var(--muted)}

/* services */
.services{top:1322px;height:466px;background:var(--pale)}
.eyebrow{font-size:13px;font-weight:700;letter-spacing:3px;color:var(--teal)}
.services .eyebrow{position:absolute;left:0;width:1200px;top:60px;text-align:center}
.services .section-heading{position:absolute;left:0;width:1200px;top:80px;text-align:center;font-size:33px;font-weight:600}
.service-card{position:absolute;top:171px;width:238px;height:215px;border-radius:4px 44px 4px 44px;overflow:hidden}
.service-card .label{position:absolute;left:0;right:0;bottom:18px;text-align:center;color:var(--white);font-weight:700;font-size:14px;letter-spacing:.5px}
.service-card.featured{background:linear-gradient(160deg,#6377c9,var(--indigo))}
.service-card.featured .inner{position:absolute;top:66px;left:0;right:0;text-align:center;color:var(--white)}
.service-card.featured h3{font-size:15px;font-weight:700;letter-spacing:.5px}
.service-card.featured p{font-size:11.5px;line-height:17px;margin:6px 22px 12px;opacity:.9}
.service-card.featured .pill{display:inline-block;padding:7px 24px;border-radius:20px;background:var(--white);color:var(--indigo);font-size:8px;font-weight:700;letter-spacing:1px}

/* about */
.about{top:1766px;height:576px;background:transparent}
.about svg{position:absolute;inset:0}
.about .eyebrow{position:absolute;left:112px;top:144px;color:var(--white);font-size:15px}
.about h2{position:absolute;left:110px;top:168px;font-size:35px;font-weight:500;color:var(--white);letter-spacing:2px}
.about h2 strong{font-weight:700}
.about p{position:absolute;left:112px;top:232px;width:440px;font-size:13.5px;line-height:29px;color:var(--white)}
.about .btn{position:absolute;left:115px;top:378px;width:231px;height:46px}

/* video */
.intro-video{top:2342px;height:556px;background:var(--white)}
.video-frame{position:absolute;left:500px;top:80px;width:586px;height:406px;border:4px solid var(--green)}
.video-thumb{position:absolute;left:103px;top:117px;width:494px;height:325px;background:linear-gradient(120deg,#3a3f47 0%,#7a7f86 40%,#d9d6d2 70%,#e9e8e6 100%);border-radius:4px}
.play{position:absolute;left:522px;top:378px;width:75px;height:64px;background:var(--indigo);display:flex;align-items:center;justify-content:center}
.intro-video .section-heading{position:absolute;left:658px;top:156px}
.intro-video p{position:absolute;left:658px;top:224px;width:390px;font-size:13.5px;line-height:27px;color:var(--text)}
.outline-btn{position:absolute;left:657px;top:356px;width:151px;height:40px;border:2px solid var(--teal);border-radius:22px;display:flex;align-items:center;justify-content:center;font-size:11px;font-weight:700;color:var(--teal);letter-spacing:1px}

/* testimonials */
.testimonials{top:2898px;height:509px;background:var(--white)}
.testimonials .section-heading{position:absolute;left:0;width:1200px;top:52px;text-align:center}
.quote-card{position:absolute;top:137px;width:292px;height:220px;background:var(--white);box-shadow:0 4px 18px rgba(30,50,70,.09);padding:50px 38px 0}
.quote-card p{font-family:'Lato',sans-serif;font-style:italic;font-size:12.5px;line-height:20px;color:var(--text)}
.stars{margin-top:18px;color:#f2b632;font-size:16px;letter-spacing:4px}
.author{position:absolute;top:374px;display:flex;align-items:center;gap:12px}
.author .avatar{width:44px;height:44px;border-radius:50%;background:linear-gradient(135deg,#e2b9a6,#b8483f)}
.author strong{display:block;font-size:12px;font-weight:700;color:var(--ink)}
.author span{font-size:11px;color:var(--muted)}

/* contact */
.contact{top:3407px;height:585px;background:var(--pale)}
.contact-photo{position:absolute;left:83px;top:73px;width:402px;height:342px;background:linear-gradient(140deg,#36a69c,#2c9a93 50%,#5cb97b)}
.contact-photo .txt{position:absolute;right:112px;top:76px;text-align:right;color:var(--white)}
.contact-photo small{font-size:12px;letter-spacing:1px;opacity:.8}
.contact-photo h2{font-size:25px;font-weight:500;line-height:31px;letter-spacing:1px}
.contact-photo h2 strong{font-weight:700}
.contact-frame{position:absolute;left:668px;top:93px;width:326px;height:382px;border:4px solid var(--green)}
.message-card{position:absolute;left:400px;top:119px;width:561px;height:387px;background:var(--white);box-shadow:0 6px 24px rgba(30,50,70,.1);padding:38px 47px}
.message-card h3{font-size:21px;font-weight:600;color:var(--ink)}
.form-field{position:absolute;width:205px}
.form-field label{display:block;font-size:13px;font-weight:500;color:var(--ink);margin-bottom:8px}
.form-field div{font-size:11px;color:var(--muted);padding-bottom:9px;border-bottom:1px solid #c9cdd2}
.send{position:absolute;left:451px;top:292px;width:58px;height:58px;border-radius:50%;background:#1e7fd0;display:flex;align-items:center;justify-content:center}

/* footer */
.site-footer{top:3992px;height:375px;background:linear-gradient(180deg,#1a9f9a,#12827e)}
.footer-logo{position:absolute;left:135px;top:70px;width:190px;display:flex;flex-direction:column;align-items:center;gap:12px}
.footer-logo .dot{width:70px;height:70px;border-radius:50%;background:var(--white)}
.footer-logo .name{font-weight:700;font-size:36px;color:var(--white)}
.divider{position:absolute;top:0;width:1px;height:313px;background:rgba(255,255,255,.18)}
.col-mark{position:absolute;width:3px;height:34px;background:var(--white);top:78px}
.footer-col{position:absolute;top:82px;color:var(--white)}
.footer-col h4{font-size:15px;font-weight:700;letter-spacing:1px;margin-bottom:12px}
.footer-col li{list-style:none;font-size:12px;line-height:27px;opacity:.95}
.contact-line{display:flex;gap:10px;font-size:12px;line-height:23px;align-items:flex-start}
.contact-line svg{flex:none;margin-top:5px}
.social{display:flex;gap:10px;margin-top:22px}
.social span{width:28px;height:28px;border-radius:50%;background:var(--white)}
.copyright{position:absolute;left:0;bottom:0;width:1200px;height:62px;background:var(--teal-deep);color:rgba(255,255,255,.85);font-size:12px;display:flex;align-items:center;justify-content:center}
</style>
</head>
<body>

<header class="site-header">
  <div class="logo-badge"><span class="dot"></span><span class="name">KESTROVA</span></div>
  <nav class="main-nav">
    <a class="active" style="left:336px">HOME</a>
    <a style="left:425px">ABOUT US</a>
    <a style="left:537px">OUR SERVICES</a>
    <a style="left:676px">WHY CHOOSE US</a>
    <a style="left:832px">TESTIMONIALS</a>
    <a style="left:971px">CONTACT US</a>
  </nav>
  <div class="call-btn">
    <svg width="13" height="13" viewBox="0 0 24 24"><path fill="#fff" d="M6.6 10.8a15 15 0 0 0 6.6 6.6l2.2-2.2c.3-.3.7-.4 1-.2 1.1.4 2.3.6 3.6.6.6 0 1 .4 1 1V20c0 .6-.4 1-1 1A17 17 0 0 1 3 4c0-.6.4-1 1-1h3.5c.6 0 1 .4 1 1 0 1.3.2 2.5.6 3.6.1.3 0 .7-.2 1z"/></svg>
    CALL US NOW +1 555 304 2178
  </div>
</header>

<section class="hero">
  <div class="hero-photo" role="img" aria-label="Therapist adjusting the shoulder of a seated senior patient"></div>
  <h1 class="hero-title">KESTROVA PHYSICAL</h1>
  <div class="hero-sub">THERAPY &amp; WELLNESS</div>
  <p class="hero-text">Lorem ipsum dolor sit amet consectetur adipiscing elit,<br>sed do eiusmod tempor incididunt</p>
  <a class="btn">BOOK APPOINTMENT</a>
  <svg class="slider-arrow" style="left:16px" viewBox="0 0 22 36"><path d="M18 3 4 18l14 15" fill="none" stroke="#1f8b8a" stroke-width="5"/></svg>
  <svg class="slider-arrow" style="left:1152px" viewBox="0 0 22 36"><path d="M4 3l14 15L4 33" fill="none" stroke="#7cc142" stroke-width="5"/></svg>
  <form class="booking">
    <h2>BOOK APPOINTMENT</h2>
    <div class="field">Your Name</div>
    <div class="field">Email Address</div>
    <div class="field">Phone Number</div>
    <div class="field">Contact Prefer time</div>
    <div class="field tall">Your Message</div>
    <div class="submit">GET QUOTE NOW</div>
  </form>
</section>

<section class="why">
  <div class="why-photo" role="img" aria-label="Therapist stretching the arm of a woman in a clinic"></div>
  <h2 class="section-heading">WHY <strong>CHOOSE KESTROVA</strong></h2>
  <div class="rule" style="left:619px;top:172px;width:62px"></div>
  <p class="lead">Lorem Ipsum is simply dummy text of the printing and typesetting industry. Lorem Ipsum has been the industry's standard</p>
  <div class="feature" style="left:607px;top:270px">
    <div class="icon"><svg width="38" height="38" viewBox="0 0 24 24" fill="none" stroke="#fff" stroke-width="1.4"><circle cx="12" cy="12" r="9"/><circle cx="12" cy="9" r="2.5"/><path d="M7 17c1-3 9-3 10 0"/></svg></div>
    <div><h3>Therapy Specialist</h3><p>Donec convallis pede venenatis nibh Duis quam</p></div>
  </div>
  <div class="feature" style="left:864px;top:268px">
    <div class="icon"><svg width="38" height="38" viewBox="0 0 24 24" fill="none" stroke="#fff" stroke-width="1.4"><path d="M12 20S4 15 4 9.5A4 4 0 0 1 12 7a4 4 0 0 1 8 2.5C20 15 12 20 12 20z"/></svg></div>
    <div><h3>Wellness Therapy</h3><p>Donec convallis pede venenatis nibh Duis quam</p></div>
  </div>
  <div class="feature" style="left:605px;top:386px">
    <div class="icon"><svg width="38" height="38" viewBox="0 0 24 24" fill="none" stroke="#fff" stroke-width="1.4"><rect x="4" y="13" width="16" height="5" rx="1"/><circle cx="12" cy="8" r="2.5"/><path d="M6 13l2-2h8l2 2"/></svg></div>
    <div><h3>Injury Pain Relief</h3><p>Donec convallis pede venenatis nibh Duis quam</p></div>
  </div>
  <div class="feature" style="left:866px;top:386px">
    <div class="icon"><svg width="38" height="38" viewBox="0 0 24 24" fill="none" stroke="#fff" stroke-width="1.4"><circle cx="12" cy="12" r="9"/><path d="M4 9c5 0 11 3 14 9M6 5c4 2 9 7 10 14M3 13c5 0 9 3 10 8"/></svg></div>
    <div><h3>Sports Therapy</h3><p>Donec convallis pede venenatis nibh Duis quam</p></div>
  </div>
</section>

<section class="services">
  <div class="eyebrow">WHAT WE DO</div>
  <h2 class="section-heading">OUR <strong>SERVICES</strong></h2>
  <div class="rule" style="left:551px;top:124px;width:96px"></div>
  <div class="service-card" style="left:90px;background:linear-gradient(160deg,#e6e9ea,#9aa6a8 60%,#3f4a4c)" role="img" aria-label="Therapist guiding a leg stretch">
    <div class="label">PHYSICAL THERAPY</div></div>
  <div class="service-card" style="left:344px;background:linear-gradient(160deg,#6a4a36,#b08a6c 55%,#2f2520)" role="img" aria-label="Massage treatment with candles">
    <div class="label">WELLNESS THERAPY</div></div>
  <div class="service-card featured" style="left:597px">
    <div class="inner"><h3>INJURY PAIN</h3><p>Lorem ipsum dolor sit amet, consectetur adipiscing</p><span class="pill">LEARN MORE</span></div></div>
  <div class="service-card" style="left:858px;background:linear-gradient(160deg,#f1efed,#c9c3bd 60%,#8a817a)" role="img" aria-label="Therapist working on a patient's knee">
    <div class="label" style="bottom:22px">JOINT RELIEF</div></div>
</section>

<section class="about">
  <svg width="1200" height="576" viewBox="0 0 1200 576">
    <defs>
      <linearGradient id="aboutTeal" x1="0" y1="0" x2="1" y2="1"><stop offset="0" stop-color="#1f8b8a"/><stop offset="1" stop-color="#2f9e8f"/></linearGradient>
      <linearGradient id="aboutPhoto" x1="0" y1="0" x2="1" y2="1"><stop offset="0" stop-color="#8fcf5a"/><stop offset=".6" stop-color="#73b94a"/><stop offset="1" stop-color="#4e9a3f"/></linearGradient>
    </defs>
    <rect x="0" y="22" width="1200" height="554" fill="url(#aboutTeal)"/>
    <path d="M520 576C560 420 550 180 640 90 700 30 770 5 860 0L1200 0V576Z" fill="#4b5fb3"/>
    <path d="M534 576C574 420 568 190 652 104 712 44 790 14 880 10 1000 6 1120 40 1200 100V576Z" fill="url(#aboutPhoto)" role="img" aria-label="Therapist examining the neck and shoulder of a woman"/>
  </svg>
  <div class="eyebrow">WHO WE ARE</div>
  <h2>ABOUT <strong>KESTROVA</strong></h2>
  <p>Lorem Ipsum is simply dummy text of the printing and typesetting industry. Lorem Ipsum has been the industry's standard dummy text ever since the 1500s, when an unknown printer took a galley of type and scrambled it to m</p>
  <a class="btn">BOOK APPOINTMENT</a>
</section>

<section class="intro-video">
  <div class="video-frame"></div>
  <div class="video-thumb" role="img" aria-label="Leg with highlighted knee joint showing pain"></div>
  <div class="play"><svg width="34" height="34" viewBox="0 0 34 34"><circle cx="17" cy="17" r="15" fill="none" stroke="#fff" stroke-width="2"/><path d="M13 10l11 7-11 7z" fill="#fff"/></svg></div>
  <h2 class="section-heading">INTRODUCTION <strong>VIDEO</strong></h2>
  <div class="rule" style="left:659px;top:195px;width:108px"></div>
  <p>Lorem Ipsum is simply dummy text of the printing and typesetting industry. Lorem Ipsum has been the industry's standard dummy text ever since the 1500s, when an unknown printer took a galley of type and</p>
  <div class="outline-btn">LEARN MORE</div>
</section>

<section class="testimonials">
  <h2 class="section-heading">WHAT <strong>OUR PEOPLE SAYS</strong></h2>
  <div class="rule" style="left:547px;top:100px;width:106px"></div>
  <div class="quote-card" style="left:125px"><p>Lorem ipsum dolor sit amet, consectetur adipiscing elit, sed do eiusmod tempor incididunt ut labore et dolore magna aliqua. Ut enim ad minim veniam, quis nostrud exercitation ullamco</p><div class="stars">★★★★★</div></div>
  <div class="quote-card" style="left:444px"><p>Lorem ipsum dolor sit amet, consectetur adipiscing elit, sed do eiusmod tempor incididunt ut labore et dolore magna aliqua. Ut enim ad minim veniam, quis nostrud exercitation ullamco</p><div class="stars">★★★★★</div></div>
  <div class="quote-card" style="left:764px"><p>Lorem ipsum dolor sit amet, consectetur adipiscing elit, sed do eiusmod tempor incididunt ut labore et dolore magna aliqua. Ut enim ad minim veniam, quis nostrud exercitation ullamco</p><div class="stars">★★★★★</div></div>
  <div class="author" style="left:134px"><div class="avatar" role="img" aria-label="Reviewer portrait"></div><div><strong>Mara Velden,</strong><span>Verified Review</span></div></div>
  <div class="author" style="left:452px"><div class="avatar" role="img" aria-label="Reviewer portrait"></div><div><strong>Ines Q.</strong><span>Customer From The Green Larder</span></div></div>
  <div class="author" style="left:773px"><div class="avatar" role="img" aria-label="Reviewer portrait"></div><div><strong>Dario Follet</strong><span>Westbrook, OR</span></div></div>
</section>

<section class="contact">
  <div class="contact-photo" role="img" aria-label="Therapist treating a patient, teal tinted">
    <div class="txt"><small>CONTACT US</small><h2>BOOK YOUR<br><strong>APPOINTMENT!</strong></h2></div>
  </div>
  <div class="contact-frame"></div>
  <form class="message-card">
    <h3>Send us a Message</h3>
    <div class="form-field" style="left:51px;top:105px"><label>Your Name</label><div>Alex Moreno</div></div>
    <div class="form-field" style="left:300px;top:105px"><label>Company</label><div>Lorem ipsum dolor sit amet</div></div>
    <div class="form-field" style="left:51px;top:188px"><label>Email &nbsp;Address</label><div>alexmoreno@mailbox.com</div></div>
    <div class="form-field" style="left:300px;top:188px"><label>Phone</label><div>01122-555-010-482</div></div>
    <div class="form-field" style="left:51px;top:272px;width:405px"><label>Message</label><div style="padding-bottom:30px">Hi, do you have a moment to talk ab...!</div></div>
    <div class="send"><svg width="22" height="22" viewBox="0 0 24 24"><path d="M22 2 2 10l7 3 3 7z" fill="#fff"/></svg></div>
  </form>
</section>

<footer class="site-footer">
  <div class="footer-logo"><span class="dot"></span><span class="name">KESTROVA</span></div>
  <div class="divider" style="left:600px"></div>
  <div class="divider" style="left:808px"></div>
  <div class="col-mark" style="left:390px"></div>
  <div class="col-mark" style="left:598px"></div>
  <div class="col-mark" style="left:806px"></div>
  <div class="footer-col" style="left:432px"><h4>NAVIGATE</h4><ul><li>Home</li><li>About Us</li><li>Our Services</li><li>New Products</li><li>Contact Us</li></ul></div>
  <div class="footer-col" style="left:629px"><h4>RESOURCES</h4><ul><li>News</li><li>Testimonials</li><li>Privacy Policy</li><li>Terms &amp; Condition</li></ul></div>
  <div class="footer-col" style="left:846px">
    <h4>CONTACT US</h4>
    <div class="contact-line"><svg width="13" height="15" viewBox="0 0 24 24"><path fill="#fff" d="M12 2a7 7 0 0 0-7 7c0 5 7 13 7 13s7-8 7-13a7 7 0 0 0-7-7zm0 9.5A2.5 2.5 0 1 1 12 6.5a2.5 2.5 0 0 1 0 5z"/></svg><span>Office Marlow | Fennick Lane 14<br>Office Ardel | Brookway 9</span></div>
    <div class="contact-line"><svg width="13" height="13" viewBox="0 0 24 24"><path fill="#fff" d="M6.6 10.8a15 15 0 0 0 6.6 6.6l2.2-2.2c.3-.3.7-.4 1-.2 1.1.4 2.3.6 3.6.6.6 0 1 .4 1 1V20c0 .6-.4 1-1 1A17 17 0 0 1 3 4c0-.6.4-1 1-1h3.5c.6 0 1 .4 1 1 0 1.3.2 2.5.6 3.6.1.3 0 .7-.2 1z"/></svg><span>Tel: (1300) 555 0187</span></div>
    <div class="contact-line"><svg width="13" height="11" viewBox="0 0 24 18"><path fill="#fff" d="M0 0h24v18H0zm2 2v.5l10 7 10-7V2z"/></svg><span>Email: info@kestrovapt.com</span></div>
    <div class="social"><span></span><span></span><span></span><span></span></div>
  </div>
  <div class="copyright">© 2021 Kestrova | All Rights Reserved &nbsp;| &nbsp;Terms &amp; Condition</div>
</footer>

</body>
</html>
```